Amazing Sexy Elegant Eyecatching Wine Label

We need a label designed for our wine which is going to be produced very soon.

Needs to be on a grey scale, as colours increase the price per label dramatically.

Needs to have the "Crown" logo (file attached) included on the front and back label. Logo can be in black/white but can not be changed in any way, circle around the crown must stay there as well.

We are still unsure of whether to use "Harrowby Wine" or "Harrowby" as the brand for the label, if you could submit designs based around the two names we would appreciate that.

We will have 5 varieties, including; Sauvignon Blanc, Chardonnay, Pinot Gris, Riesling and Pinot Noir. So text needs to be easily changed.

We are after an image on the label which is modern and eye catching, even in a grey scale.

Please see other attached files for an idea we have done previously, we want something a bit more "designer" though. Some information on the label is a legal requirement and needs to be kept.

Target Market(s)

Wine Consumers

Requirements
Must have
• Crown Logo, Harrowby/Harrowby Wine brand, Grey Scale, Modern Design

```html
<!DOCTYPE html>
<html lang="en">
<head>
<meta charset="utf-8">
<title>Harrowby Wine – Marlborough Sauvignon Blanc Label</title>
<link rel="stylesheet" href="https://fonts.googleapis.com/css2?family=Raleway:wght@400;500&display=swap">
<style>
  :root {
    --canvas: #ffffff;
    --label-black: #141414;
    --label-dark: #1d1d1d;
    --label-sheen: #6a6a6a;
    --ink-silver: #a3a3a3;
    --frame-silver: #8c8c8c;
    --mountain-grey: #9a9a9a;
  }
  html, body {
    margin: 0;
    padding: 0;
    width: 1200px;
    height: 1000px;
    overflow: hidden;
    background: var(--canvas);
  }
  .canvas {
    position: relative;
    width: 1200px;
    height: 1000px;
  }
  .wine-label {
    position: absolute;
    left: 400px;
    top: 190px;
    width: 400px;
    height: 620px;
    display: block;
  }
  .label-text {
    font-family: "Raleway", sans-serif;
    fill: var(--ink-silver);
    text-anchor: middle;
  }
  .brand-name { font-size: 33px; font-weight: 400; letter-spacing: 4px; }
  .brand-mark-name { font-size: 13px; font-weight: 500; letter-spacing: 1.5px; }
  .region, .variety { font-size: 19px; font-weight: 500; letter-spacing: 2px; }
  .vintage { font-size: 22px; font-weight: 400; letter-spacing: 3px; }
  .origin { font-size: 11px; font-weight: 500; letter-spacing: 3px; }
</style>
</head>
<body>
<main class="canvas">
  <svg class="wine-label" viewBox="0 0 400 620" xmlns="http://www.w3.org/2000/svg" aria-labelledby="label-title">
    <title id="label-title">Harrowby Wine Marlborough Sauvignon Blanc 2015 label</title>
    <defs>
      <radialGradient id="top-sheen" cx="0.5" cy="1" r="0.75">
        <stop offset="0" stop-color="var(--label-sheen)"/>
        <stop offset="1" stop-color="var(--label-black)"/>
      </radialGradient>
      <radialGradient id="bottom-glow" cx="0.5" cy="0.35" r="0.6">
        <stop offset="0" stop-color="#9a9a9a"/>
        <stop offset="1" stop-color="var(--label-black)"/>
      </radialGradient>
    </defs>

    <!-- label base -->
    <rect class="label-base" x="0" y="0" width="400" height="620" fill="var(--label-black)"/>
    <rect class="label-top-band" x="0" y="0" width="400" height="168" fill="url(#top-sheen)"/>
    <rect class="label-bottom-glow" x="0" y="560" width="400" height="60" fill="url(#bottom-glow)"/>

    <!-- arched frame panel -->
    <path class="label-frame"
          d="M58 83 H135 C140 58 170 41 205 41 C240 41 270 58 275 83 H343 V578 H58 Z"
          fill="var(--label-dark)" stroke="var(--frame-silver)" stroke-width="2"/>

    <!-- brand mark -->
    <circle class="brand-mark" cx="205" cy="118" r="49" fill="none" stroke="var(--ink-silver)" stroke-width="4"/>
    <text class="label-text brand-mark-name" x="205" y="123">HARROWBY</text>

    <!-- brand name -->
    <text class="label-text brand-name" x="205" y="220">HARROWBY</text>
    <text class="label-text brand-name" x="205" y="258">WINE</text>

    <!-- mountain illustration area -->
    <rect class="mountain-art" x="103" y="346" width="187" height="31" rx="2"
          fill="var(--mountain-grey)" role="img" aria-label="Silhouette of a mountain range"/>

    <!-- wine details -->
    <text class="label-text region" x="205" y="422">MARLBOROUGH</text>
    <text class="label-text variety" x="205" y="450">SAUVIGNON BLANC</text>
    <text class="label-text vintage" x="205" y="486">2015</text>
    <text class="label-text origin" x="205" y="546">WINE OF NEW ZEALAND</text>
  </svg>
</main>
</body>
</html>
```